Hello Creative Minds!
Our business is after a elegant and classy flyer that draws attention!
The business is Velmora Turf - Lawn Rejuvenation Services. We provide services that maintain a healthy and vibrant green lawn through the tough Australian seasons. The products we use limits the water needed to keep grass green to a minimum - practically none at all! This not only helps the home owner or home seller but the environment by limiting the use of water that is needed to create a green lawn. The products we use are made from natural ingredients that are and pet friendly.
This fly will be our introductory offer to the market. Below are the required points that need to be on the flyer. Attached is the business logo, before & after pictures and 1 example of the LAYOUT not DESIGN of what the flyer should be laid out like or similar to. Feel free to use different 'Lawn Mower' pictures.
All the best; if you need any questions answered please feel free to message.
REQUIRED POINTS (Please re-phrase were possible);
*Instantly restores the natural green colour of grass – year round
*Lasts for up to 3 months
*Substantially reduces watering needs
*Pet friendly
*Stays green during droughts and water restrictions
*UV fade resistant
*Won’t bleed, run, or stain once absorbed into the grass
*Safe for the environment, pets and people
*Works in extreme heat, cold and frost
*Organic and natural – no harmful chemicals
*Reduces the amount of fertilizer
and water used on lawns
*Kerb appeal is essential for getting your property sold for the highest price possible
SERVICES & PRICING
Lawn maintenance (cut & trim) starting from $60
Lawn rejuvenation starting from $80 (Only $27 a month for 3 months)*
Package deal starting from $120
Introductory offer: 25% off all services. Refer a friend, when they book you receive another 25% off your next service.
LOCATIONS
Nowra to Sydney
CONTACT NUMBER
Will be posted with the winner - please leave an area for this.
SOCIAL MEDIA
Please add Chatterloop and Snapvista logo's
Updates
Competition has finished, thank you to all that have participated! I will review and comment on the flyers that need assistance. All the best with future designs!
Target Market(s)
home owners, home sellers, property developers, real estates and nursing homes and government housing.
Industry/Entity Type
Lawn Care
Look and feel
Each slider illustrates characteristics of the customer's brand and the style your logo design should communicate.

```html
<!DOCTYPE html>
<html lang="en">
<head>
<meta charset="utf-8">
<title>Velmora Turf - Lawn Rejuvenation Services</title>
<link rel="stylesheet" href="https://fonts.googleapis.com/css2?family=Dosis:wght@500;700;800&family=Open+Sans:wght@400;600;700&display=swap">
<style>
  :root {
    --charcoal: #2b2d30;
    --charcoal-deep: #1c1d1f;
    --lime: #8cc63f;
    --lime-light: #d9ecbf;
    --forest: #2f6b1e;
    --grass-dark: #2d5a14;
    --grass-mid: #4f8f22;
    --grass-light: #8fc24a;
    --white: #ffffff;
    --ink: #2a2a2a;
    --before-red: #d8231f;
    --after-green: #6fb02c;
  }
  * { box-sizing: border-box; margin: 0; padding: 0; }
  html, body { width: 900px; height: 1200px; overflow: hidden; background: var(--white); }
  .flyer { position: relative; width: 900px; height: 1200px; font-family: "Open Sans", sans-serif; color: var(--ink); }

  .brand-header {
    height: 170px; background: linear-gradient(180deg, var(--charcoal) 0%, var(--charcoal-deep) 100%);
    text-align: center; padding-top: 34px;
  }
  .brand-name { font-family: "Dosis", sans-serif; font-weight: 700; font-size: 66px; color: var(--white); line-height: 1; letter-spacing: 1px; }
  .brand-tagline { font-family: "Dosis", sans-serif; font-weight: 500; font-size: 17px; letter-spacing: 7px; color: var(--lime); margin-top: 12px; }

  .hero { position: relative; height: 460px; overflow: hidden; }
  .hero-photo {
    position: absolute; inset: 0;
    background: linear-gradient(180deg, var(--grass-dark) 0%, var(--grass-mid) 45%, var(--grass-light) 100%);
  }
  .hero-swoosh { position: absolute; left: 0; bottom: 0; width: 900px; height: 140px; }
  .offers { position: absolute; left: 40px; top: 36px; color: var(--white); font-family: "Dosis", sans-serif; }
  .offer { margin-bottom: 26px; }
  .offer-title { font-weight: 800; font-size: 44px; line-height: 1; }
  .offer-line { display: flex; align-items: flex-end; gap: 16px; margin-top: 6px; }
  .offer-note { font-weight: 700; font-size: 22px; line-height: 1.2; }
  .offer-price { font-weight: 800; font-size: 70px; line-height: 0.9; }

  .package-band { background: var(--lime-light); height: 60px; border-top: 6px solid var(--lime); text-align: center; }
  .package-title { font-family: "Dosis", sans-serif; font-weight: 800; font-size: 38px; color: var(--forest); line-height: 54px; }
  .intro-offer { text-align: center; padding-top: 12px; font-size: 15px; line-height: 1.45; }
  .intro-offer strong { font-weight: 700; }

  .results { display: flex; gap: 14px; padding: 20px 40px 0; }
  .result-pair { flex: 1; display: flex; gap: 6px; }
  .result-shot { position: relative; flex: 1; height: 145px; }
  .result-shot.dry { background: linear-gradient(160deg, #b9a77a 0%, #8f7d52 100%); }
  .result-shot.lush { background: linear-gradient(160deg, #6fa83a 0%, #3e7a1e 100%); }
  .result-shot.bare { background: linear-gradient(160deg, #9a9470 0%, #6b6a56 100%); }
  .result-shot.neat { background: linear-gradient(160deg, #5f9c34 0%, #6a6f6a 100%); }
  .result-label {
    position: absolute; left: 0; bottom: 0; padding: 2px 12px; font-size: 14px; font-weight: 700; color: var(--white);
  }
  .result-label.before { background: var(--before-red); }
  .result-label.after { background: var(--after-green); }

  .benefits { display: flex; gap: 30px; padding: 20px 40px 0 48px; }
  .benefit-list { flex: 1; list-style: none; }
  .benefit-list li { position: relative; padding-left: 18px; font-size: 14px; font-weight: 600; line-height: 1.32; margin-bottom: 2px; }
  .benefit-list li::before { content: ""; position: absolute; left: 0; top: 7px; width: 7px; height: 7px; border-radius: 50%; background: var(--ink); }

  .contact-bar {
    position: absolute; left: 0; bottom: 0; width: 900px; height: 66px; background: var(--lime);
    display: flex; align-items: center; justify-content: center; gap: 14px;
    font-family: "Dosis", sans-serif; font-weight: 700; font-size: 24px; color: var(--charcoal-deep);
  }
</style>
</head>
<body>
<div class="flyer">
  <header class="brand-header">
    <div class="brand-name">Velmora Turf</div>
    <div class="brand-tagline">LAWN REJUVENATION SERVICES</div>
  </header>

  <section class="hero">
    <div class="hero-photo" role="img" aria-label="Red ride-on lawn mower cutting a lush green lawn"></div>
    <svg class="hero-swoosh" viewBox="0 0 900 140" preserveAspectRatio="none" aria-hidden="true">
      <path d="M0 40 C 220 140, 520 150, 900 110 L900 140 L0 140 Z" fill="#2f6b1e" opacity="0.85"/>
      <path d="M0 80 C 260 150, 560 150, 900 130 L900 140 L0 140 Z" fill="#8cc63f"/>
    </svg>
    <div class="offers">
      <div class="offer">
        <div class="offer-title">LAWN MAINTENANCE</div>
        <div class="offer-line">
          <div class="offer-note">(CUT &amp; TRIM)<br>STARTING FROM</div>
          <div class="offer-price">$60</div>
        </div>
      </div>
      <div class="offer">
        <div class="offer-title">LAWN REJUVENATION</div>
        <div class="offer-line">
          <div class="offer-note">STARTING FROM<br>(ONLY $27 A<br>MONTH FOR 3 MONTHS)*</div>
          <div class="offer-price">$80</div>
        </div>
      </div>
    </div>
  </section>

  <section class="package-band">
    <div class="package-title">PACKAGE DEAL STARTING FROM $120</div>
  </section>
  <p class="intro-offer"><strong>Introductory offer: 25% off all services.</strong><br>Refer a friend, when they book you receive another 25% off your next service.</p>

  <section class="results">
    <div class="result-pair">
      <div class="result-shot dry" role="img" aria-label="Dry brown lawn before treatment"><span class="result-label before">before</span></div>
      <div class="result-shot lush" role="img" aria-label="Green lawn after treatment"><span class="result-label after">after</span></div>
    </div>
    <div class="result-pair">
      <div class="result-shot bare" role="img" aria-label="Faded front lawn before treatment"><span class="result-label before">before</span></div>
      <div class="result-shot neat" role="img" aria-label="Restored front lawn after treatment"><span class="result-label after">after</span></div>
    </div>
  </section>

  <section class="benefits">
    <ul class="benefit-list">
      <li>Instantly restores the natural green colour of grass – year round</li>
      <li>Lasts for up to 3 months</li>
      <li>Substantially reduces watering needs</li>
      <li>Pet friendly</li>
      <li>Stays green during droughts and water restrictions</li>
      <li>UV fade resistant</li>
    </ul>
    <ul class="benefit-list">
      <li>Won't bleed, run, or stain once absorbed into the grass</li>
      <li>Safe for the environment, pets and people</li>
      <li>Works in extreme heat, cold and frost</li>
      <li>Organic and natural – no harmful chemicals</li>
      <li>Reduces the amount of fertilizer and water used on lawns</li>
      <li>Kerb appeal is essential for getting your property sold for the highest price possible</li>
    </ul>
  </section>

  <footer class="contact-bar">
    <span>Add: Nowra to Sydney</span><span>|</span><span>Call: 0482 615 903</span><span>|</span><span>Chatterloop Snapvista</span>
  </footer>
</div>
</body>
</html>
```